Plakat-Design für podologische therapeutische Praxis
Zielgruppe
Wir sind eine podologische therapeutische Praxis für medizinische Fußbehandlungen.
Wir haben eine Kassenzulassung und versorgen ausschließlich Risikopatienten z.B. Diabetiker ect.
Unser Schwerpunkt ist die Behandlung von diabetischen Füßen ( Diab. Fußsyndrom ), eingewachsen und entzündliche Fußnägel, Nagelkorrekturen und künstlicher Nagelaufbau.
Zielgruppe sind alle Menschen von Jung - alt die schmerzen, Entzündungen an den Zehennägel haben und Hilfe suchen.
Aufgabenstellung
Das Plakat soll speziell auf die Behandlung von eingewachsenen Fußnägel ausgerichtet sein und nicht zu viele Informationen enthalten. Vll. eine Schlagzeile ' PROBLEME MIT EINGEWACHSEN FUßNÄGEL ? HIER DIE LÖSUNG ....
( Die individuelle Nagelspangenkorrektur ) Ihre Vorteile: Individuell angepasste Spangensysteme, schnelle Schmerzlinderung, Keine Einschränkung im Alltag, Alternative zur Operation.. Jetzt Termin vereinbaren ---- PODOLOGIE WESTERFELD
Gestaltung vll. in Form einer lustigen Unterhaltung oder animierten Menschen ( Zeichnung ). es kann aber auch etwas ganz anderes sein....
Es soll aber trotzdem einen medizinischen Charakter vorhanden sein.
Anbei mein Firmenlogo als Datei.
HOMEPAGE: www.podologie-westerfeld-beispiel.de
Ich möchte ein Plakat erstellen es aber auch als normalen Flyer nutzen können.
Vielen Dank für die Vorschläge.

```html
<!DOCTYPE html>
<html lang="de">
<head>
<meta charset="utf-8">
<title>Plakat – Podologie Westerfeld</title>
<link href="https://fonts.googleapis.com/css2?family=Montserrat:wght@700&family=Pathway+Gothic+One&family=Roboto:wght@400;500;700&display=swap" rel="stylesheet">
<style>
  :root{
    --navy:#005f80;
    --brand:#0b5a7a;
    --teal:#55aab3;
    --green:#8db51f;
    --white:#ffffff;
    --page:#e4e4e4;
  }
  html,body{margin:0;padding:0;width:1200px;height:1200px;overflow:hidden;background:var(--page);}
  .poster{position:absolute;left:180px;top:24px;width:840px;height:1152px;background:var(--white);overflow:hidden;font-family:"Roboto",Arial,sans-serif;}
  .shapes{position:absolute;left:0;top:0;width:840px;height:1152px;}
  .brand{position:absolute;left:0;width:840px;text-align:center;}
  .brand-mark{position:absolute;left:386px;top:70px;width:68px;height:68px;background:var(--teal);border-radius:6px;}
  .brand-name{top:190px;font-family:"Montserrat",Arial,sans-serif;font-weight:700;font-size:34px;letter-spacing:1px;color:var(--brand);}
  .photo{position:absolute;left:454px;top:298px;width:314px;height:314px;border-radius:50%;
    background:radial-gradient(circle at 40% 35%,#c7d9f0 0%,#a9c6e8 35%,#e8c2ad 70%,#dcae97 100%);}
  .headline{position:absolute;left:55px;top:596px;margin:0;font-family:"Pathway Gothic One","Arial Narrow",sans-serif;font-weight:400;font-size:92px;line-height:82px;color:var(--white);white-space:nowrap;letter-spacing:0;transform:scaleX(0.84);transform-origin:left top;}
  .solution{position:absolute;left:58px;top:827px;width:318px;height:130px;border:2px solid var(--white);border-radius:8px;box-sizing:border-box;text-align:center;padding-top:13px;color:var(--white);font-weight:500;font-size:25px;line-height:35px;}
  .solution .lead{color:var(--green);font-weight:700;}
  .benefits{position:absolute;left:463px;top:806px;color:var(--white);}
  .benefits h2{margin:0 0 8px;font-size:19px;font-weight:500;color:var(--green);}
  .benefits ul{list-style:none;margin:0;padding:0;}
  .benefits li{display:flex;align-items:center;height:36px;font-size:15.5px;font-weight:500;}
  .benefits svg{width:17px;height:17px;margin:0 14px 0 2px;}
  .footer-contact{position:absolute;left:0;top:1022px;width:419px;height:130px;background:var(--teal);color:var(--white);font-size:15px;}
  .footer-contact .row{position:absolute;left:73px;}
  .footer-contact svg{position:absolute;left:-22px;top:3px;width:13px;height:13px;}
  .footer-contact .name{top:28px;font-weight:700;}
  .footer-contact .addr{top:51px;}
  .footer-contact .web{top:78px;}
  .footer-cta{position:absolute;left:419px;top:1022px;width:421px;height:130px;background:var(--green);color:var(--white);}
  .footer-cta .call{position:absolute;left:70px;top:38px;font-size:18px;font-weight:500;}
  .footer-cta .phone{position:absolute;left:70px;top:62px;font-size:31px;font-weight:700;white-space:nowrap;}
  .footer-cta svg{position:absolute;left:36px;top:70px;width:24px;height:24px;}
</style>
</head>
<body>
<div class="poster">
  <svg class="shapes" viewBox="0 0 953 1307" preserveAspectRatio="none" aria-hidden="true">
    <path fill="#005f80" d="M0,342 C40,480 150,570 270,567 C370,564 440,530 510,497 A188 188 0 0 1 840,432 C900,445 940,480 953,505 L953,1307 L0,1307 Z"/>
  </svg>

  <div class="brand-mark"></div>
  <div class="brand brand-name">PODOLOGIE WESTERFELD</div>

  <div class="photo" role="img" aria-label="Foto: Behandlung eines eingewachsenen Zehennagels mit Instrument und Handschuhen"></div>

  <h1 class="headline">PROBLEME MIT<br>EINGEWACHSENEN FUßNÄGELN?</h1>

  <div class="solution">
    <div class="lead">Wir haben die Lösung</div>
    <div>Die individuelle</div>
    <div>Nagelspangentherapie</div>
  </div>

  <div class="benefits">
    <h2>Ihre Vorteile</h2>
    <ul>
      <li><svg viewBox="0 0 20 20"><circle cx="10" cy="10" r="8" fill="none" stroke="#8db51f" stroke-width="1.6"/><path d="M6 10.5l3 3 7-8" fill="none" stroke="#8db51f" stroke-width="1.8"/></svg>Individuell angepasste Spangensysteme</li>
      <li><svg viewBox="0 0 20 20"><circle cx="10" cy="10" r="8" fill="none" stroke="#8db51f" stroke-width="1.6"/><path d="M6 10.5l3 3 7-8" fill="none" stroke="#8db51f" stroke-width="1.8"/></svg>schnelle Schmerzlinderung</li>
      <li><svg viewBox="0 0 20 20"><circle cx="10" cy="10" r="8" fill="none" stroke="#8db51f" stroke-width="1.6"/><path d="M6 10.5l3 3 7-8" fill="none" stroke="#8db51f" stroke-width="1.8"/></svg>Keine Einschränkung im Alltag</li>
      <li><svg viewBox="0 0 20 20"><circle cx="10" cy="10" r="8" fill="none" stroke="#8db51f" stroke-width="1.6"/><path d="M6 10.5l3 3 7-8" fill="none" stroke="#8db51f" stroke-width="1.8"/></svg>Alternative zur Operation.</li>
    </ul>
  </div>

  <div class="footer-contact">
    <div class="row name"><svg viewBox="0 0 16 16"><path d="M8 1a4 4 0 0 1 4 4c0 3-4 7-4 7S4 8 4 5a4 4 0 0 1 4-4z" fill="none" stroke="#fff" stroke-width="1.4"/><circle cx="8" cy="5" r="1.4" fill="#fff"/><path d="M3 14h10" stroke="#fff" stroke-width="1.4"/></svg>PODOLOGIE WESTERFELD</div>
    <div class="row addr">Lindenweg 14, 12345 Musterstadt</div>
    <div class="row web"><svg viewBox="0 0 16 16"><circle cx="8" cy="8" r="6.5" fill="none" stroke="#fff" stroke-width="1.3"/><ellipse cx="8" cy="8" rx="3" ry="6.5" fill="none" stroke="#fff" stroke-width="1.1"/><path d="M1.5 8h13" stroke="#fff" stroke-width="1.1"/></svg>www.podologie-westerfeld-beispiel.de</div>
  </div>

  <div class="footer-cta">
    <div class="call">Jetzt Termin vereinbaren!</div>
    <svg viewBox="0 0 24 24"><path d="M6 3l3 4-2 2c1 2.5 3.5 5 6 6l2-2 4 3-2 3C10 18 6 14 3 6z" fill="none" stroke="#fff" stroke-width="1.6" stroke-linejoin="round"/><path d="M14 3a7 7 0 0 1 7 7M14 6.5a3.5 3.5 0 0 1 3.5 3.5" fill="none" stroke="#fff" stroke-width="1.5"/></svg>
    <div class="phone">Tel.: 01234 - 5678901</div>
  </div>
</div>
</body>
</html>
```